create clean, simple business card template

using the logo created now we need to create a simple, elegant business card design to suit

Industry/Entity Type

Business

Font styles to use
Other font styles liked:
• segoe ui

Requirements
Must have
• Front:
"Name:"
"Title:"
"Mobile:"
"email:"
and the logo

Back:
Logo
Nice to have
• Text in black but other graphics etc to match colours in logo as provided

```html
<!DOCTYPE html>
<html lang="en">
<head>
<meta charset="utf-8">
<title>Keller &amp; Tate Homes — Business Card</title>
<link href="https://fonts.googleapis.com/css2?family=Open+Sans:wght@400;600;700&display=swap" rel="stylesheet">
<style>
  :root {
    --page-bg: #e9e6e1;
    --card-bg: #ffffff;
    --brand-brown: #7b6440;
    --text-dark: #5a5a5a;
    --divider: #cfcfcf;
    --mark-grey: #9a9a9a;
    --shadow: rgba(0, 0, 0, 0.28);
  }
  * { margin: 0; padding: 0; box-sizing: border-box; }
  html, body {
    width: 1200px;
    height: 1045px;
    overflow: hidden;
    background: var(--page-bg);
    font-family: "Open Sans", "Segoe UI", sans-serif;
  }
  .card {
    position: absolute;
    left: 258px;
    width: 698px;
    height: 400px;
    background: var(--card-bg);
    box-shadow: 3px 4px 8px var(--shadow);
  }
  .card--front { top: 80px; }
  .card--back { top: 521px; }

  .brand {
    position: absolute;
    display: flex;
    align-items: center;
    gap: 12px;
    font-weight: 600;
    white-space: nowrap;
  }
  .brand__dot {
    width: 22px;
    height: 22px;
    border-radius: 50%;
    background: currentColor;
    flex: none;
  }
  .card--front .brand {
    left: 40px;
    top: 181px;
    font-size: 25px;
    color: var(--brand-brown);
  }
  .card--back .brand {
    left: 0;
    right: 0;
    top: 180px;
    justify-content: center;
    font-size: 30px;
    color: var(--mark-grey);
  }

  .divider {
    position: absolute;
    left: 364px;
    top: 117px;
    width: 1px;
    height: 184px;
    background: var(--divider);
  }

  .contact {
    position: absolute;
    left: 419px;
    top: 100px;
    color: var(--text-dark);
    font-size: 17px;
    line-height: 25.5px;
  }
  .contact__name {
    font-size: 21px;
    font-weight: 700;
    color: var(--brand-brown);
    line-height: 30px;
  }
  .contact__title { margin-bottom: 16px; }
  .contact__label {
    font-weight: 700;
    color: var(--brand-brown);
  }
  .contact__web { color: var(--brand-brown); }
</style>
</head>
<body>
  <section class="card card--front">
    <div class="brand"><span class="brand__dot"></span>Keller &amp; Tate Homes</div>
    <div class="divider"></div>
    <div class="contact">
      <p class="contact__name">Lorem Ipsum Dollar</p>
      <p class="contact__title">Managing Director</p>
      <p>4210 Harbor Oak Lane # 220</p>
      <p>Lakeview, FL 33901</p>
      <p><span class="contact__label">T:</span> 14820 331 275</p>
      <p><span class="contact__label">F:</span> 14820 331 275</p>
      <p><span class="contact__label">E:</span> hello@kellertatehomes.com</p>
      <p class="contact__web">www.kellertatehomes.com</p>
    </div>
  </section>

  <section class="card card--back">
    <div class="brand"><span class="brand__dot"></span>Keller &amp; Tate Homes</div>
  </section>
</body>
</html>
```